今回はコーポレートサイトのTOPページのデザインをお願いしたく思います。

【素材】
素材に関しては、ロゴや写真等は現在準備中でして、
デザインの際は仮のオブジェクトを入れて対応して頂ければと思います。

【サイト構成】
サイトの構成については、ラフを書きましたので下記URLからダウンロードお願いします。
http://qvn.jp/PbLwoR

※PCを想定したデザインでお願いいたします。

【イメージ】
以下が現在の「アオバエステート株式会社」のコーポレートサイトになります。
http://www.aoba-estate.co.jp/

今回ご提案いただく新しいサイトのデザインは上記のものから一新して

1.スタイリッシュ
2.NY
3.最先端
4.近未来
5.エネルギッシュ
6.エキサイティング
7.自由
8.それでいてシンプル

なイメージ、従来の不動産会社のイメージに囚われないものにしたく思います。

【参考サイト】
https://www.kumonomi.co.jp/

1ページ
グレー系
今回のデザインで採用させて頂いた方には、
コーポレートサイトの「代表メッセージ」「ニュース」「投資実績」の他3ページのデザインやコーディングなど、他のお仕事に関してもご相談させて頂ければと思います。
(もちろん当案件のみご希望の方からも募集しており、採用有無には関係ありません。)

色のコンセプトと対応の早さ、デザインの良さで決定致しました。

皆さま、お忙しい所多くのご提案を頂きまして誠にありがとうございます。
また何かございましたらお願いをさせて頂きますので引き続き宜しくお願い致します。

```html
<!DOCTYPE html>
<html lang="ja">
<head>
<meta charset="utf-8">
<title>AOBA | 不動産の新しい未来をつくる</title>
<link href="https://fonts.googleapis.com/css2?family=Noto+Serif+JP:wght@400;600&family=Noto+Sans+JP:wght@400;700&family=Oswald:wght@500;700&display=swap" rel="stylesheet">
<style>
:root{
  --navy:#0f1b3d;
  --ink:#222;
  --grey-text:#666;
  --pale:#f2f2f2;
  --black:#0a0a0a;
  --white:#fff;
  --line:#ddd;
}
*{box-sizing:border-box;margin:0;padding:0}
html,body{width:1200px;height:5192px;overflow:hidden}
body{font-family:"Noto Sans JP",sans-serif;color:var(--ink);background:var(--white);position:relative}
.abs{position:absolute}
.ph{position:absolute}
/* header */
.site-header{left:0;top:0;width:1200px;height:72px;background:var(--navy);display:flex;align-items:center;justify-content:space-between;padding:0 40px}
.brand{font-family:"Oswald",sans-serif;font-weight:700;font-size:34px;color:var(--white);letter-spacing:1px}
.global-nav{display:flex;gap:44px;font-size:15px;color:var(--white);letter-spacing:1px}
/* hero */
.hero{left:0;top:72px;width:1200px;height:1216px;background:linear-gradient(180deg,#eef0f3 0%,#c9ced6 55%,#a9b0ba 100%)}
.hero-name{left:0;top:460px;width:1200px;text-align:center;font-family:"Oswald",sans-serif;font-weight:700;font-size:170px;color:var(--navy);letter-spacing:6px;line-height:1}
.hero-copy{left:0;top:680px;width:1200px;text-align:center;font-family:"Noto Serif JP",serif;font-size:56px;color:var(--ink)}
.hero-notice{right:0;top:1168px;width:232px;height:48px;background:rgba(255,255,255,.35);color:var(--white);font-size:13px;display:flex;align-items:center;justify-content:center}
/* intro */
.intro{left:0;top:1288px;width:1200px;height:424px;text-align:center}
.intro h2{font-family:"Noto Serif JP",serif;font-weight:400;font-size:46px;margin-top:92px}
.intro p{font-size:16px;line-height:30px;color:var(--grey-text);margin-top:40px}
/* concept */
.concept-title{left:80px;top:2370px;font-family:"Noto Serif JP",serif;font-size:40px;color:var(--white);letter-spacing:2px}
.concept-text{left:80px;top:2450px;width:440px;font-size:14px;line-height:26px;color:#ddd}
.btn{display:flex;align-items:center;justify-content:center;gap:18px;font-size:14px;color:var(--white);background:var(--black)}
.concept-btn{left:200px;top:2598px;width:200px;height:48px}
/* work & news */
.work{left:0;top:2820px;width:800px;height:628px;background:var(--white)}
.sec-title{position:absolute;font-family:"Noto Serif JP",serif;font-size:44px;letter-spacing:2px}
.more{position:absolute;font-size:13px;color:var(--grey-text)}
.work-card{position:absolute;top:188px;width:190px}
.work-card .thumb{height:128px}
.work-card h3{font-size:15px;font-weight:700;line-height:26px;margin-top:16px}
.work-card p{font-size:12px;line-height:22px;color:var(--grey-text);margin-top:10px}
.work-card time{display:block;font-size:12px;color:#aaa;margin-top:14px}
.news{left:800px;top:2820px;width:400px;height:628px;background:var(--black);color:var(--white)}
.news-item{position:absolute;left:68px;font-size:13px;line-height:22px;color:#ccc}
.news-item time{display:block;color:#999}
/* construction */
.construct{left:600px;top:3448px;width:600px;height:512px;background:var(--pale)}
.construct h2{position:absolute;left:96px;top:172px;font-family:"Noto Serif JP",serif;font-weight:400;font-size:44px}
.construct p{position:absolute;left:96px;top:252px;width:420px;font-size:14px;line-height:26px;color:var(--grey-text)}
.construct .btn{left:196px;top:410px;width:200px;height:52px}
/* footer nav */
.foot-nav{left:208px;top:4030px;width:800px;display:flex;justify-content:space-between}
.foot-nav dl{width:110px}
.foot-nav dt{font-size:14px;font-weight:700;margin-bottom:14px}
.foot-nav dd{font-size:12px;color:var(--grey-text);line-height:26px}
.map{left:32px;top:4260px;width:1136px;height:520px;background:linear-gradient(135deg,#eceae4,#dfe6e0)}
.map-card{left:46px;top:4274px;width:330px;height:110px;background:var(--white);box-shadow:0 1px 4px rgba(0,0,0,.25);padding:14px 18px;font-size:13px;line-height:20px;color:#333}
.footer{left:0;top:4780px;width:1200px;height:348px;background:var(--pale);text-align:center}
.footer .brand-row{margin-top:96px;display:flex;justify-content:center;align-items:center;gap:22px}
.footer .brand-row span{font-family:"Oswald",sans-serif;font-weight:700;font-size:52px;color:var(--navy)}
.footer address{font-style:normal;font-size:13px;line-height:22px;color:var(--grey-text);margin-top:22px}
.social{display:flex;justify-content:center;gap:18px;margin-top:22px}
.social i{width:18px;height:18px;border-radius:50%;background:var(--navy);display:block}
.bottom-bar{left:0;top:5128px;width:1200px;height:64px;background:var(--navy);color:var(--white);display:flex;align-items:center;padding:0 36px;font-size:15px}
.bottom-bar .cta{margin-left:auto;background:var(--white);color:var(--navy);font-weight:700;height:40px;padding:0 30px;display:flex;align-items:center;font-size:14px}
.bottom-bar .close{margin-left:30px;font-size:20px}
</style>
</head>
<body>

<header class="abs site-header">
  <div class="brand">AOBA</div>
  <nav class="global-nav"><span>TOP</span><span>ABOUT</span><span>WORK</span><span>NEWS</span><span>CONTACT</span></nav>
</header>

<section class="ph hero" role="img" aria-label="夕暮れの高層ビル群とタワーを見下ろす都市の写真"></section>
<div class="abs hero-name">AOBA</div>
<div class="abs hero-copy">不動産の新しい未来をつくる</div>
<div class="abs hero-notice">AOBAのお知らせはこちら ›</div>

<section class="abs intro">
  <h2>不動産の新しい未来をつくる</h2>
  <p>AOBAのサブテキストを入れてくださいAOBAのサブテキストを入れてください<br>
  AOBAのサブテキストを入れてくださいAOBAのサブテキストを入れてくださいAOBAのサブテキストを入れてください<br>
  AOBAのサブテキストを入れてくださいAOBAのサブテキストを入れてくださいAOBAのサブテキスト<br>
  AOBAのサブテキストを入れてくださいAOBAのサブテキストを入れてください。</p>
</section>

<div class="ph" style="left:0;top:1712px;width:400px;height:492px;background:linear-gradient(160deg,#cfd9e2,#eef1f2 60%,#9aa88e)" role="img" aria-label="白い外観のモダンな住宅の写真"></div>
<div class="ph" style="left:400px;top:1712px;width:400px;height:492px;background:linear-gradient(135deg,#3c4e6a,#8796ab 55%,#d9dee5)" role="img" aria-label="ビジネスの握手の写真"></div>
<div class="ph" style="left:800px;top:1712px;width:400px;height:492px;background:linear-gradient(160deg,#7fb4e4,#dfe4ea 55%,#b8bcc2)" role="img" aria-label="住宅模型と設計図の写真"></div>
<div class="ph" style="left:0;top:2204px;width:600px;height:616px;background:linear-gradient(135deg,#4a3f38,#6e625a 50%,#2f2a27)" role="img" aria-label="打ち合わせをする人物の写真（暗めの背景）"></div>
<div class="ph" style="left:600px;top:2204px;width:600px;height:616px;background:linear-gradient(135deg,#e9e9ea,#c8ccd2 50%,#3f4a66)" role="img" aria-label="資料を見ながら相談する男女の写真"></div>

<div class="abs concept-title">CONCEPT</div>
<p class="abs concept-text">私達が目指すのは、お客様一人ひとりの暮らしに寄り添う住まいづくりです。土地探しから設計、施工、アフターサービスまで一貫して対応し、安心と信頼をお届けします。新しい発想で未来の街をつくります。</p>
<div class="abs btn concept-btn">コンセプト<span>›</span></div>

<section class="abs work">
  <h2 class="sec-title" style="left:64px;top:118px">WORK</h2>
  <span class="more" style="left:616px;top:136px">WORK一覧 ›</span>
  <article class="work-card" style="left:64px"><div class="thumb" style="background:linear-gradient(180deg,#9cc3e8,#d4d9d2)" role="img" aria-label="造成された分譲地の写真"></div><h3>物件に関するテキスト物件に関するテキスト物件に関するテキスト物件</h3><p>物件に関するテキスト物件に関するテキスト物件に関するテキスト物件</p><time>2019.00.00</time></article>
  <article class="work-card" style="left:304px"><div class="thumb" style="background:linear-gradient(180deg,#b9c6d3,#6b6560)" role="img" aria-label="新築住宅の外観写真"></div><h3>物件に関するテキスト物件に関するテキスト物件に関するテキスト物件</h3><p>物件に関するテキスト物件に関するテキスト物件に関するテキスト物件</p><time>2019.00.00</time></article>
  <article class="work-card" style="left:544px"><div class="thumb" style="background:linear-gradient(180deg,#a8cbe9,#b8b3a2)" role="img" aria-label="住宅地の空き区画の写真"></div><h3>物件に関するテキスト物件に関するテキスト物件に関するテキスト物件</h3><p>物件に関するテキスト物件に関するテキスト物件に関するテキスト物件</p><time>2019.00.00</time></article>
  <svg class="abs" style="left:758px;top:248px" width="20" height="40" viewBox="0 0 20 40"><path d="M4 4 L16 20 L4 36" fill="none" stroke="#333" stroke-width="2"/></svg>
</section>

<section class="abs news">
  <h2 class="sec-title" style="left:68px;top:118px;color:#fff">NEWS</h2>
  <div class="news-item" style="top:200px"><time>2019.10.24</time>新着物件のご案内を掲載しました<br>ぜひご覧ください</div>
  <div class="news-item" style="top:282px"><time>2019.10.24</time>定休日のお知らせ</div>
  <div class="news-item" style="top:340px"><time>2019.10.22</time>見学会の開催についてのお知らせ<br>詳細は各ページをご確認ください</div>
  <span class="news-item" style="top:424px">お知らせ一覧 ›</span>
</section>

<div class="ph" style="left:0;top:3448px;width:600px;height:512px;background:linear-gradient(135deg,#4d4641,#7d766e 55%,#b7b3ac)" role="img" aria-label="施工した住宅の玄関と植栽の写真"></div>
<section class="abs construct">
  <h2>Construction example</h2>
  <p>施工例に関するテキストが入ります施工例に関するテキストが入ります施工例に関するテキストが入ります施工例に関するテキストが入ります施工例に関するテキストが入ります。</p>
  <div class="abs btn">施 工 例</div>
</section>

<nav class="abs foot-nav">
  <dl><dt>HOME</dt><dd>ホーム</dd></dl>
  <dl><dt>ABOUT</dt><dd>企業情報</dd><dd>会社概要</dd><dd>アクセス</dd></dl>
  <dl><dt>WORK</dt><dd>サブページ</dd><dd>サブページ</dd><dd>サブページ</dd></dl>
  <dl><dt>NEWS</dt><dd>サブページ</dd><dd>サブページ</dd><dd>サブページ</dd></dl>
  <dl><dt>CONTACT</dt><dd>サブページ</dd><dd>サブページ</dd></dl>
  <dl><dt>CONTACT</dt><dd>お問い合わせ</dd></dl>
</nav>

<div class="ph map" role="img" aria-label="本社所在地周辺の地図"></div>
<svg class="abs" style="left:586px;top:4496px" width="28" height="40" viewBox="0 0 28 40"><path d="M14 0C6 0 0 6 0 14c0 10 14 26 14 26s14-16 14-26C28 6 22 0 14 0z" fill="#d93a32"/><circle cx="14" cy="14" r="5" fill="#fff"/></svg>
<div class="abs map-card"><b>〒150-0042 架空県青葉市若葉町3-8-2</b><br>〒150-0042 架空県青葉市若葉町3丁目8-2<br><span style="color:#1a73e8">拡大地図を表示</span></div>

<footer class="abs footer">
  <div class="brand-row"><span style="font-family:'Noto Sans JP',sans-serif;font-size:40px">ロゴ</span><span>AOBA</span></div>
  <address>〒150-0042 架空県青葉市若葉町3丁目8-2　TEL 000-123-4567（代表）<br>FAX 000-123-4568　営業時間 10:00～19:00 定休日 水曜日（祝日を除く）</address>
  <div class="social"><i></i><i></i><i></i><i></i></div>
</footer>

<div class="abs bottom-bar">
  <span>AOBAのお知らせ!内覧会ツアーを実施中！期間：2019/00/00～2019/00/00</span>
  <span class="cta">資料請求のお問い合わせ ›</span>
  <span class="close">×</span>
</div>

</body>
</html>
```